Infographic to communicate Cyber Security and Insurance Product Offering for IT Service Providers

We need an inspirational infographic that shows how VaultBridge works with KRE (an MSP partner) to help organisations close the loop on cyber risk. The design should illustrate the layers of the IT infrastructure stack and the systems and processes that wrap around it to protect and mitigate against risk.
At the core: MSP Services (Desktop, Software, Website). Surrounding this: VaultBridge Governance & Protection, leading into an Incident layer that connects to VaultBridge Insurance and Incident Response, linked by a continuous feedback loop. The outer circle should represent the constant threat of cyber attack.
VaultBridge core offerings for this graphic:
Shield Attest (compliance/assurance product)
Shield Cover
KRE Primary Services (directly connected to VaultBridge):
Managed IT Services
Disaster Recovery as a Service (DRaaS)
E8 Security Packages
Cloud Hosting & Infrastructure
KRE Secondary Services (supporting but not directly anchored):
Telephony & Unified Communications
Networking Services
Data Backup & Storage Solutions
Professional Services & Consulting
Procurement & Licensing
Training & User Awareness
Style: Modern, professional, and client-friendly, with a technology-inspired colour palette.
Deliverables: Polished colour version plus editable source files — preferably in Figma, or alternatively if not possible using either Adobe Illustrator (.AI) or a layered Photoshop (.PSD) (e.g. industry standards for editable design).
Rewards: The winning design prize will be increased by $100, and we will also award $50 each to the 2nd and 3rd place runner-ups, as our way of giving a little more back.
A simple wireframe visual guide has been uploaded as a reference, but this should in no way limit or restrict your creativity. We encourage original, innovative approaches to bring this concept to life.
Ownership & Exclusivity: As per ArtFolio’s T&Cs, all rights to the winning design will transfer to us once the project is complete for our ongoing use. We also kindly ask that the work created here remain exclusive to this project, meaning it won’t be reused or lightly modified for other clients in the future. The reason is simple: once we’ve invested in and paid for a design, we want to be confident it won’t turn up on a competitor’s website with just a different colour scheme. Thanks again for respecting that. [Note:- The designs submitted so far haven’t quite hit the mark, so I’ve put together a couple of slides to clarify direction. These outline the key stakeholders, the current IT services and challenges, how the Brimlox product addresses those challenges, and a simple version of what we’d like the infographic to convey. Please review these slides carefully, as they should give you a clearer understanding of the story we want the design to tell.]
Target Market(s)
Small to Medium sized businesses
Colors
Designer to choose colors to be used in the design.
Look and feel

```html
<!DOCTYPE html>
<html lang="en">
<head>
<meta charset="utf-8">
<title>VaultBridge – Closing the Loop on Cyber Risk</title>
<link rel="stylesheet" href="https://fonts.googleapis.com/css2?family=Open+Sans:wght@600;700&display=swap">
<style>
  :root {
    --backdrop: #a9fdfd;
    --navy: #03276f;
    --ring: #33b6ca;
    --teal-top: #31aab2;
    --blue-bottom: #0d57aa;
    --tile-top: #36c9bd;
    --tile-mid: #2fb9bc;
    --tile-low: #2592b8;
    --badge: #0b4fa6;
    --box: #0a4a9e;
    --loop: #0e4ba2;
    --shield: #37c3cf;
    --white: #ffffff;
  }
  * { margin: 0; padding: 0; box-sizing: border-box; }
  html, body { width: 1200px; height: 1200px; overflow: hidden; background: var(--backdrop); }
  .canvas { display: block; width: 1200px; height: 1200px; }
  .canvas text { font-family: "Open Sans", sans-serif; fill: var(--white); text-anchor: middle; }
  .heading { font-size: 40px; font-weight: 600; letter-spacing: 1px; }
  .threat-label { font-size: 60px; font-weight: 700; }
  .core-title { font-size: 50px; font-weight: 600; letter-spacing: 1px; }
  .layer-label { font-size: 36px; font-weight: 700; letter-spacing: 1px; }
  .service-label { font-size: 28px; font-weight: 600; }
  .incident-label { font-size: 50px; font-weight: 700; letter-spacing: 1px; }
  .insurance-label { font-size: 38px; font-weight: 700; }
  .response-label { font-size: 34px; font-weight: 700; }
  .footer-title { font-size: 66px; font-weight: 700; }
  .icon { fill: none; stroke: var(--white); stroke-width: 4; stroke-linecap: round; stroke-linejoin: round; }
</style>
</head>
<body>
<svg class="canvas" viewBox="0 0 1932 1932" xmlns="http://www.w3.org/2000/svg">
  <defs>
    <linearGradient id="core-fill" x1="0" y1="0" x2="0" y2="1">
      <stop offset="0" stop-color="var(--teal-top)"/>
      <stop offset="1" stop-color="var(--blue-bottom)"/>
    </linearGradient>
    <linearGradient id="tile-head" x1="0" y1="0" x2="0" y2="1">
      <stop offset="0" stop-color="var(--tile-top)"/>
      <stop offset="1" stop-color="#2aa7b5"/>
    </linearGradient>
    <radialGradient id="badge-fill" cx="0.4" cy="0.35" r="0.7">
      <stop offset="0" stop-color="#0f5cb6"/>
      <stop offset="1" stop-color="#0a469a"/>
    </radialGradient>
    <linearGradient id="loop-right" x1="0" y1="0" x2="1" y2="1">
      <stop offset="0" stop-color="#2aa3c4"/>
      <stop offset="1" stop-color="#0e4ba2"/>
    </linearGradient>
  </defs>

  <!-- poster card -->
  <rect class="poster" x="353" y="54" width="1273" height="1842" fill="#0a2a55" opacity="0.35"/>
  <rect class="poster" x="347" y="48" width="1273" height="1842" fill="var(--navy)"/>

  <!-- cyber attack ring -->
  <g class="threat-ring" fill="none" stroke="var(--ring)" stroke-width="9" stroke-linecap="round">
    <path d="M640 1116 A538 538 0 1 1 1452 452"/>
    <path d="M1428 440 L1452 456 L1458 428"/>
    <path d="M1490 886 A538 538 0 0 1 1324 1118"/>
  </g>
  <text class="threat-label" transform="translate(1474 675) rotate(90)">CYBER ATTACK</text>

  <!-- governance heading -->
  <g class="governance-shield" fill="none" stroke="var(--shield)" stroke-width="6" stroke-linejoin="round" stroke-linecap="round">
    <path d="M978 210 C1005 228 1030 232 1032 232 L1032 275 C1032 305 1010 320 978 332 C946 320 924 305 924 275 L924 232 C928 232 952 228 978 210 Z"/>
    <path d="M978 222 C1000 237 1020 241 1020 241 L1020 275 C1020 298 1003 310 978 320 C953 310 936 298 936 275 L936 241 C940 241 958 237 978 222 Z"/>
    <path d="M956 272 L973 288 L1000 258"/>
  </g>
  <text class="heading" x="978" y="387">VAULTBRIDGE</text>
  <text class="heading" x="978" y="440">GOVERNANCE &amp; PROTECTION</text>

  <!-- core services stack -->
  <rect class="core" x="713" y="480" width="539" height="502" rx="130" fill="url(#core-fill)"/>
  <rect class="core-tile" x="807" y="537" width="350" height="395" rx="20" fill="var(--tile-low)"/>
  <path class="core-tile-head" d="M827 537 H1137 A20 20 0 0 1 1157 557 V715 H807 V557 A20 20 0 0 1 827 537 Z" fill="url(#tile-head)"/>
  <rect class="core-layer" x="807" y="718" width="350" height="67" fill="var(--tile-mid)"/>
  <rect class="core-layer" x="807" y="789" width="350" height="66" fill="var(--tile-mid)"/>
  <text class="core-title" x="982" y="614">KRE MSP</text>
  <text class="core-title" x="978" y="671">SERVICES</text>
  <text class="layer-label" x="982" y="764">DESKTOP</text>
  <text class="layer-label" x="982" y="832">SOFTWARE</text>
  <text class="layer-label" x="982" y="909">WEBSITE</text>

  <!-- service badges -->
  <g class="service-badges" fill="url(#badge-fill)">
    <circle cx="622" cy="553" r="70"/>
    <circle cx="623" cy="798" r="70"/>
    <circle cx="1341" cy="555" r="70"/>
    <circle cx="1342" cy="797" r="70"/>
    <circle cx="760" cy="1045" r="70"/>
    <circle cx="983" cy="1080" r="70"/>
    <circle cx="1207" cy="1045" r="70"/>
  </g>

  <!-- managed IT icon -->
  <g class="icon">
    <rect x="609" y="518" width="53" height="42"/>
    <path d="M625 560 V575 M612 577 H662"/>
    <rect x="598" y="531" width="28" height="22" fill="var(--badge)"/>
    <rect x="583" y="562" width="37" height="25" fill="var(--badge)"/>
  </g>
  <!-- telephony icon -->
  <g class="icon">
    <path d="M618 836 C600 818 586 805 586 787 A32 32 0 0 1 650 787 C650 795 647 801 643 807"/>
    <circle cx="618" cy="787" r="10"/>
    <circle cx="640" cy="822" r="18"/>
    <circle cx="640" cy="822" r="6"/>
  </g>
  <!-- security lock icon -->
  <g class="lock-icon">
    <path d="M1318 545 V533 A23 23 0 0 1 1364 533 V545" fill="none" stroke="var(--white)" stroke-width="7"/>
    <rect x="1306" y="542" width="70" height="56" rx="6" fill="var(--white)"/>
    <circle cx="1341" cy="564" r="8" fill="var(--badge)"/>
    <rect x="1337" y="566" width="8" height="16" rx="3" fill="var(--badge)"/>
  </g>
  <!-- cloud icon -->
  <g class="icon">
    <path d="M1300 822 H1376 A18 18 0 0 0 1378 786 A26 26 0 0 0 1330 778 A18 18 0 0 0 1302 792 A15 15 0 0 0 1300 822 Z"/>
    <circle cx="1354" cy="812" r="12"/>
    <path d="M1354 795 V799 M1354 825 V829 M1337 812 H1341 M1367 812 H1371 M1342 800 L1345 803 M1363 821 L1366 824 M1366 800 L1363 803 M1345 821 L1342 824"/>
  </g>
  <!-- backup icon -->
  <g class="icon">
    <path d="M724 1030 C740 1012 772 1010 792 1025"/>
    <path d="M797 1066 C780 1082 748 1084 728 1068"/>
    <path d="M730 1056 L790 1062 M740 1040 L792 1026 M740 1040 L790 1062"/>
    <circle cx="790" cy="1062" r="5" fill="var(--white)"/>
    <circle cx="730" cy="1056" r="5" fill="var(--white)"/>
    <circle cx="792" cy="1026" r="4" fill="var(--white)"/>
    <circle cx="727" cy="1024" r="3" fill="var(--white)"/>
  </g>
  <!-- networking icon -->
  <g class="icon">
    <circle cx="983" cy="1060" r="14"/>
    <path d="M955 1082 H1011 M983 1090 V1113"/>
    <circle cx="960" cy="1103" r="10"/>
    <circle cx="1007" cy="1103" r="10"/>
  </g>
  <!-- consulting icon -->
  <g class="icon">
    <circle cx="1207" cy="1045" r="33" stroke-width="6"/>
    <path d="M1195 1050 C1198 1058 1204 1062 1212 1062 L1216 1056 L1210 1052 L1206 1054 C1202 1050 1200 1046 1200 1042 L1203 1038 L1198 1032 L1193 1036 C1192 1042 1193 1046 1195 1050 Z" fill="var(--white)"/>
    <path d="M1214 1030 L1213 1052" stroke-width="5"/>
  </g>

  <!-- service labels -->
  <text class="service-label" x="610" y="660">Managed</text>
  <text class="service-label" x="610" y="695">IT Services</text>
  <text class="service-label" x="625" y="907">Telephony &amp;</text>
  <text class="service-label" x="625" y="943">Unified Comms</text>
  <text class="service-label" x="1350" y="660">Esaas</text>
  <text class="service-label" x="1350" y="697">B Security</text>
  <text class="service-label" x="1347" y="908">Cloud Hosting</text>
  <text class="service-label" x="1347" y="946">&amp; Infrastructure</text>
  <text class="service-label" x="741" y="1158">Data Backup</text>
  <text class="service-label" x="741" y="1194">&amp; Storage</text>
  <text class="service-label" x="983" y="1193">Networking</text>
  <text class="service-label" x="983" y="1229">Services</text>
  <text class="service-label" x="1230" y="1158">Professional</text>
  <text class="service-label" x="1230" y="1194">Services &amp;</text>
  <text class="service-label" x="1230" y="1230">Consulting</text>

  <!-- incident feedback loop -->
  <g class="feedback-loop" fill="none" stroke-width="6" stroke-linecap="round">
    <path d="M795 1314 C700 1330 630 1370 633 1420 C636 1470 700 1500 788 1516" stroke="var(--loop)"/>
    <path d="M1172 1316 C1250 1326 1330 1370 1334 1424" stroke="url(#loop-right)"/>
    <path d="M1318 1408 L1334 1428 L1352 1408" stroke="#1d78b8"/>
    <path d="M1326 1446 C1300 1490 1240 1508 1178 1518" stroke="var(--loop)"/>
  </g>
  <rect class="incident-box" x="795" y="1274" width="375" height="66" rx="4" fill="var(--box)"/>
  <text class="incident-label" x="982" y="1321">INCIDENT</text>

  <rect class="insurance-box" x="788" y="1381" width="392" height="116" rx="8" fill="var(--box)"/>
  <g class="icon" stroke-width="3.5">
    <path d="M843 1403 C856 1412 867 1413 868 1413 V1438 C868 1455 857 1463 843 1470 C829 1463 818 1455 818 1438 V1413 C819 1413 830 1412 843 1403 Z"/>
    <path d="M843 1462 V1430 M830 1442 L843 1430 L856 1442"/>
  </g>
  <text class="insurance-label" x="1018" y="1435">VAULTBRIDGE</text>
  <text class="insurance-label" x="1018" y="1478">INSURANCE</text>

  <rect class="response-box" x="781" y="1532" width="413" height="60" rx="4" fill="var(--box)"/>
  <text class="response-label" x="992" y="1576">INCIDENT RESPONSE</text>

  <!-- footer title -->
  <text class="footer-title" x="980" y="1702">VAULTBRIDGE - CLOSING THE</text>
  <text class="footer-title" x="982" y="1768">LOOP ON CYBER RISK</text>
</svg>
</body>
</html>
```